VALTIRO.NET Single Product Based Website

We are one of the largest Stockiest of Diesel Engine (Marine and Power Plants) Spare Parts, this site will be focusing on a Single Product / Spare Parts - Connecting Rods <br/>We attached some actual pictures of the product and the Logo,<br/><br/>Once we approved your design shall provide with some contends and 10 actual Pictures to be added , should be a single page website SEO friendly sources to be used<br/>Should be Desktop, laptop and mobile friendly <br/><br/>best regards<br/>Oliver <br/>

Coding

Coded - Design and coding required

Number of Pages Required

1 page

Font styles to use
Other font styles liked:
• Book Antigua, Book Man Old Style or the designer can suggest

Colors

Designer to choose colors to be used in the design.

Requirements
Must have
• The Logo and same theme / colors can be used
Nice to have
• We shall provide the actual pictures of the product from our gallery approx 10 pictures to be added at final stage
Should not have
• other than initial design purpose , do not use any pictures downloaded from the internet

```html
<!DOCTYPE html>
<html lang="en">
<head>
<meta charset="utf-8">
<title>VALTIRO.NET – Connecting Rods</title>
<link rel="stylesheet" href="https://fonts.googleapis.com/css2?family=Libre+Baskerville:wght@400;700&family=Open+Sans:wght@400;600;700&display=swap">
<style>
:root{
  --blue:#2b4a8a;
  --blue-dark:#24407a;
  --orange:#f04e31;
  --ink:#1b1b1b;
  --white:#ffffff;
  --grey-photo:#8a8a8a;
  --footer-bar:#0d0d0d;
  --line:#d9d9d9;
}
*{box-sizing:border-box;margin:0;padding:0}
html,body{width:1200px;height:2745px;overflow:hidden;background:var(--white)}
body{position:relative;font-family:"Libre Baskerville","Book Antiqua",Georgia,serif;color:var(--ink)}
.abs{position:absolute}
a{color:inherit;text-decoration:none}

/* header */
.topbar{top:20px;right:72px;display:flex;align-items:center;gap:14px}
.icon-circle{width:36px;height:36px;border-radius:50%;background:#efefef;display:flex;align-items:center;justify-content:center}
.phone{display:flex;align-items:center;gap:8px;font-family:"Open Sans",Arial,sans-serif;font-weight:700;font-size:25px;color:var(--ink);margin-right:4px}
.cart-count{position:absolute;top:-4px;right:-6px;font-family:"Open Sans",Arial,sans-serif;font-size:12px}
.nav{top:110px;font-size:15px;display:flex;gap:35px;letter-spacing:.3px}
.nav-left{left:160px}
.nav-right{left:801px;top:105px}
.brand{top:92px;left:450px;width:300px;text-align:center;font-weight:700;font-size:34px;color:var(--blue);letter-spacing:1px}

/* hero */
.hero{top:165px;left:0;width:1200px;height:429px}
.hero-title{top:300px;left:734px;font-size:33px;color:var(--white)}
.hero-text{top:343px;left:735px;width:330px;font-size:15.5px;line-height:22px;color:var(--white)}
.btn{display:inline-flex;align-items:center;justify-content:center;border-radius:25px;color:var(--white);font-size:18px}
.hero-btn{top:433px;left:731px;width:144px;height:48px;background:var(--blue)}
.dots{top:542px;left:752px;display:flex;gap:12px}
.dots span{width:8px;height:8px;border-radius:50%;background:#1f1fd0}

/* usp band */
.usp{top:594px;left:0;width:1200px;height:181px;background:var(--blue);display:flex}
.usp-item{flex:1;display:flex;flex-direction:column;align-items:center;justify-content:center;color:var(--white);border-right:1px solid #6f86b5}
.usp-item:last-child{border-right:none}
.usp-item:first-child{padding-left:130px}
.usp-item:last-child{padding-right:0}
.usp-title{font-size:26px;margin-top:12px;letter-spacing:.5px}
.usp-sub{font-size:11px;font-weight:700;margin-top:10px;letter-spacing:.4px}

/* sections */
.section-title{font-size:36px;letter-spacing:.5px;color:var(--ink)}
.prod-photo{top:895px;left:72px;width:517px;height:397px;background:linear-gradient(135deg,#e3c13a,#d4ad22 60%,#c89f1d)}
.price-tag{top:895px;left:72px}
.card{top:939px;left:535px;width:591px;height:304px;background:var(--white);box-shadow:0 0 6px rgba(0,0,0,.15);padding:46px 47px}
.card h3{font-weight:400;font-size:33px;letter-spacing:.3px}
.card p{font-size:15.5px;line-height:22px;margin-top:10px;width:490px}
.selects{display:flex;gap:26px;margin-top:16px}
.select{width:160px;height:51px;border:1px solid var(--line);box-shadow:0 1px 3px rgba(0,0,0,.15);display:flex;align-items:center;justify-content:space-between;padding:0 18px;font-size:15px}
.price-btn{margin-top:17px;width:181px;height:48px;background:var(--orange);font-size:18px}
.price-btn small{font-size:11px;margin-right:3px}

.gallery-arrows{top:1403px;left:1063px;display:flex;gap:22px}
.thumb{top:1457px;width:241px;height:203px}

/* blog */
.blog{top:1707px;left:62px;width:1064px;height:385px}
.blog-title{top:1748px;left:669px;font-size:32px;color:var(--white)}
.blog-sub{top:1794px;left:641px;font-size:18px;color:var(--white)}
.blog-text{top:1840px;left:641px;width:420px;font-size:15.5px;line-height:22px;color:var(--white)}
.blog-btn{top:1976px;left:647px;width:162px;height:48px;background:var(--orange)}

/* newsletter */
.news-title{top:2141px;left:0;width:1200px;text-align:center;font-size:32px;letter-spacing:.5px}
.email{top:2208px;left:254px;width:535px;height:51px;border:2px solid #e6e6e6;border-radius:26px;display:flex;align-items:center;padding-left:28px;font-size:13px;box-shadow:0 1px 3px rgba(0,0,0,.1)}
.subscribe{top:2209px;left:800px;width:144px;height:48px;background:var(--orange)}

/* footer */
.footer{top:2332px;left:0;width:1200px;height:351px;background:var(--blue);color:var(--white)}
.f-col{position:absolute;top:76px}
.f-head{font-size:26px;letter-spacing:.3px}
.f-list{list-style:none;margin-top:12px;margin-left:4px;font-size:13px;line-height:27.5px}
.f-phone{font-size:25px}
.f-hours{font-size:13px;margin-top:6px;margin-left:4px}
.f-brand{margin-top:55px;margin-left:4px;font-weight:700;font-size:32px;letter-spacing:1px}
.bottom{top:2683px;left:0;width:1200px;height:62px;background:var(--footer-bar);color:#9a9a9a;font-family:"Open Sans",Arial,sans-serif;font-size:13px}
.bottom .copy{position:absolute;left:75px;top:22px}
.cards{position:absolute;right:75px;top:18px;display:flex;gap:32px}
.cards span{width:32px;height:24px;background:#6a6a6a;border-radius:3px}
</style>
</head>
<body>

<header>
  <div class="abs topbar">
    <span class="phone">
      <span class="icon-circle">
        <svg width="14" height="14" viewBox="0 0 24 24"><path d="M6.6 10.8a15 15 0 006.6 6.6l2.2-2.2c.3-.3.7-.4 1-.2 1.1.4 2.3.6 3.6.6.6 0 1 .4 1 1V20c0 .6-.4 1-1 1A17 17 0 013 4c0-.6.4-1 1-1h3.5c.6 0 1 .4 1 1 0 1.3.2 2.5.6 3.6.1.3 0 .7-.2 1z" fill="#111"/></svg>
      </span>1-800-555-0142</span>
    <span class="icon-circle"><svg width="14" height="14" viewBox="0 0 24 24"><circle cx="12" cy="7" r="5" fill="#111"/><path d="M2 23c0-6 4.5-9 10-9s10 3 10 9z" fill="#111"/></svg></span>
    <span class="icon-circle"><svg width="14" height="14" viewBox="0 0 24 24"><circle cx="10" cy="10" r="6.5" fill="none" stroke="#111" stroke-width="3"/><path d="M15 15l6 6" stroke="#111" stroke-width="3.5" stroke-linecap="round"/></svg></span>
    <span class="icon-circle" style="position:relative"><svg width="16" height="14" viewBox="0 0 24 22"><path d="M1 2h4l3 12h12l3-9H7" fill="none" stroke="#111" stroke-width="2.5"/><path d="M7 5h16l-3 9H9z" fill="#111"/><circle cx="10" cy="19" r="2" fill="#111"/><circle cx="19" cy="19" r="2" fill="#111"/></svg><span class="cart-count">0</span></span>
  </div>
  <nav class="abs nav nav-left"><a href="#">HOME</a><a href="#">ABOUT US</a><a href="#">SHOP</a></nav>
  <div class="abs brand">VALTIRO.NET</div>
  <nav class="abs nav nav-right"><a href="#">PRODUCT</a><a href="#">GALLERY</a><a href="#">CONTACT</a></nav>
</header>

<section>
  <svg class="abs hero" viewBox="0 0 1200 429" preserveAspectRatio="none">
    <rect width="1200" height="429" fill="#7d7d7d" role="img" aria-label="Photo of a polished connecting rod on a grey textured surface"/>
    <path d="M670 20 C700 5 760 25 800 18 C860 8 900 0 920 0 C905 20 870 35 875 60 C885 85 960 60 1040 40 C1110 22 1170 5 1200 0 L1200 429 L678 429 C660 380 645 330 655 290 C665 240 680 200 675 150 C670 100 650 55 670 20 Z" fill="var(--orange)"/>
  </svg>
  <h1 class="abs hero-title" style="font-weight:400">VALTIRO.NET</h1>
  <p class="abs hero-text">Neque porro quisquam est qui dolorem ipsum quia dolor sit amet, consectetur, adipisci velit...</p>
  <a class="abs btn hero-btn" href="#">SHOP NOW</a>
  <div class="abs dots"><span></span><span></span><span></span></div>
</section>

<section class="abs usp">
  <div class="usp-item" style="padding-left:130px;flex:1.08">
    <svg width="36" height="28" viewBox="0 0 36 28"><rect x="0" y="2" width="22" height="18" rx="2" fill="#fff"/><path d="M22 8h8l6 7v5H22z" fill="#fff"/><circle cx="8" cy="22" r="4" fill="#fff" stroke="var(--blue)" stroke-width="2"/><circle cx="28" cy="22" r="4" fill="#fff" stroke="var(--blue)" stroke-width="2"/></svg>
    <div class="usp-title">FREE SHIPPING</div>
    <div class="usp-sub">ON ORDERS OVER $XX</div>
  </div>
  <div class="usp-item" style="flex:1">
    <svg width="34" height="30" viewBox="0 0 34 30"><rect x="1" y="6" width="32" height="23" rx="2" fill="#fff"/><path d="M5 1h24l4 5H1z" fill="#fff"/><rect x="5" y="13" width="3" height="9" fill="var(--blue)"/><rect x="10" y="13" width="3" height="9" fill="var(--blue)"/><rect x="15" y="13" width="3" height="9" fill="var(--blue)"/><path d="M22 17h7M22 17l3-3M22 17l3 3" stroke="var(--blue)" stroke-width="2" fill="none"/></svg>
    <div class="usp-title">EASY RETURNS</div>
    <div class="usp-sub">XX DAY HASSLE &nbsp;- FREE RETURNS</div>
  </div>
  <div class="usp-item" style="flex:1.04">
    <svg width="34" height="32" viewBox="0 0 34 32"><path d="M17 1C8 1 1 7 1 15c0 4 2 7 5 10l-3 6 8-3c2 1 4 1 6 1 9 0 16-6 16-14S26 1 17 1z" fill="#fff"/><text x="17" y="21" text-anchor="middle" font-family="Open Sans,Arial,sans-serif" font-weight="700" font-size="16" fill="var(--blue)">$</text></svg>
    <div class="usp-title">OTHER USP</div>
    <div class="usp-sub">OTHER USP DETAILS</div>
  </div>
</section>

<section>
  <h2 class="abs section-title" style="top:828px;left:100px;font-weight:400">PRODUCTS</h2>
  <div class="abs prod-photo" role="img" aria-label="Photo of three numbered connecting rods on a yellow sheet"></div>
  <svg class="abs price-tag" width="170" height="165" viewBox="0 0 170 165"><path d="M0 0H170L0 165Z" fill="var(--blue)"/><text x="27" y="62" font-family="Open Sans,Arial,sans-serif" font-weight="700" font-size="30" fill="#fff">$50</text></svg>
  <div class="abs card">
    <h3>CONNECTING RODS</h3>
    <p>Neque porro quisquam est qui dolorem ipsum quia dolor sit amet, consectetur, adipisci velit...</p>
    <div class="selects">
      <div class="select">Size <svg width="12" height="8" viewBox="0 0 12 8"><path d="M1 1l5 5 5-5" stroke="#111" stroke-width="2.5" fill="none"/></svg></div>
      <div class="select" style="padding-left:26px">QTY <svg width="12" height="8" viewBox="0 0 12 8"><path d="M1 1l5 5 5-5" stroke="#111" stroke-width="2.5" fill="none"/></svg></div>
    </div>
    <a class="btn price-btn" href="#"><small>OUR PRICE :</small>$50.00</a>
  </div>
</section>

<section>
  <h2 class="abs section-title" style="top:1366px;left:98px;font-weight:400">GALLERY</h2>
  <div class="abs gallery-arrows">
    <svg width="12" height="16" viewBox="0 0 12 16"><path d="M9 2L3 8l6 6" stroke="#111" stroke-width="3" fill="none"/></svg>
    <svg width="12" height="16" viewBox="0 0 12 16"><path d="M3 2l6 6-6 6" stroke="#111" stroke-width="3" fill="none"/></svg>
  </div>
  <div class="abs thumb" style="left:72px;background:linear-gradient(160deg,#8a7e70,#5a5249)" role="img" aria-label="Photo of rows of connecting rods laid out on a floor"></div>
  <div class="abs thumb" style="left:346px;background:linear-gradient(160deg,#6e6760,#a7a39d)" role="img" aria-label="Close-up photo of a connecting rod big end with bolt"></div>
  <div class="abs thumb" style="left:613px;background:linear-gradient(160deg,#8a5a40,#9b9b98)" role="img" aria-label="Close-up photo of a connecting rod bearing bore"></div>
  <div class="abs thumb" style="left:886px;background:linear-gradient(160deg,#c7a57f,#6a6a66)" role="img" aria-label="Photo of two labelled connecting rods on cardboard"></div>
</section>

<section>
  <svg class="abs blog" viewBox="0 0 1064 385" preserveAspectRatio="none">
    <rect width="1064" height="385" fill="var(--blue)"/>
    <path d="M0 0H350C450 20 530 80 532 180C533 260 500 330 560 385H0Z" fill="var(--orange)"/>
    <path d="M0 0H330C430 25 510 85 510 180C510 270 480 335 540 385H0Z" fill="#7b7b7b" role="img" aria-label="Photo of a connecting rod big end on a grey textured surface"/>
  </svg>
  <h2 class="abs blog-title" style="font-weight:400">BLOG</h2>
  <div class="abs blog-sub">CONNECTING RODS</div>
  <p class="abs blog-text">Neque porro quisquam est qui dolorem ipsum quia dolor sit amet, consectetur, adipisci Lorem ipsum dolor sit amet, consectetur adipiscing elit, sed do eiusmod tempor incididunt ut labore et dolore magna aliqua. Ut enim ad minim veniam,velit...</p>
  <a class="abs btn blog-btn" href="#">READ MORE</a>
</section>

<section>
  <h2 class="abs news-title" style="font-weight:400">SUBSCRIBE NEWSLETTER</h2>
  <div class="abs email">EMAIL</div>
  <a class="abs btn subscribe" href="#">SUBSCRIBE</a>
</section>

<footer class="abs footer">
  <div class="f-col" style="left:72px">
    <div class="f-phone">1-800 555 0142</div>
    <div class="f-hours">Available From &nbsp;9am to 5 pm EST</div>
    <div class="f-brand">VALTIRO.NET</div>
  </div>
  <div class="f-col" style="left:406px">
    <div class="f-head">LINKS</div>
    <ul class="f-list"><li>Home</li><li>About Us</li><li>Products</li><li>Blog</li><li>Contact Us</li></ul>
  </div>
  <div class="f-col" style="left:635px">
    <div class="f-head">SHOP BY BRAND</div>
    <ul class="f-list" style="margin-top:9px"><li>Brand Name 1</li><li>Brand Name 2</li><li>Brand Name Longer 3</li><li>Brand Name Even Longer 4</li><li>See All Brands</li></ul>
  </div>
  <div class="f-col" style="left:968px">
    <div class="f-head">INFO</div>
    <ul class="f-list" style="margin-top:9px"><li>Terms &amp; Conditions</li><li>Returns</li><li>Privacy policy</li><li>Sitemap</li></ul>
  </div>
</footer>
<div class="abs bottom">
  <span class="copy">© 2020 &nbsp;| &nbsp;www.valtiro-parts.com</span>
  <div class="cards"><span></span><span></span><span></span><span></span></div>
</div>

</body>
</html>
```